Flyer für Weingut
Zielgruppe
Wir sind das Familien Weingut Kolbe aus der Südpalz und wohnen direkt in der Holunderstraße. Eine Straße die viele Touristen anzieht. Wir möchten dieses Jahr das erste mal einen art Gutsauschank eröffnen. Indem es kleinigkeiten zu Essen und unseren Wein zu trinken gibt. Wir möchten sowohl die Touristen einfangen aber auch vorallem einheimische aus den nachbar Orten als Kunden gewinnen. Jeder ist willkomen von jung bis alt.
Aufgabenstellung
modern, ansprechend, professionell, klar, strukuriert, besonders.
Öffnungszeiten unseres Ausschanks: Mittwoch bis Sonntag ab 22.08.25 bis 02.11.25 von 14-20 Uhr
Es gibts kleinigkeiten zu essen zum beispiel Flammkuchen, Pfälzer Tapas oder auch Gemische Wurst/Käse Platten. Getränke: Offene Weine oder Flaschenweine, Weinschorle. Die Essensauswahl soll nicht genaustens aufgelistet werden. Es reicht zum Beispiel: Kleinigkeiten zum Essen oder ähnliches.
Zusatzinfos: Kleiner Hof mit Gartenmöbel. Platz für ca. 50 Leute. Kleine Louge Ecke mit Loungemöbeln. Es gibt nur Selbstbedienung. Gemütliche, lockere Atmosphäre. Vielfältige Weinauswahl.
Wir möchten speziell von Mischgetränken Abstand nehmen. Wir als Familienweingut stehen hinter unserem Produkt und möchten vorallem auch den jungen Leuten den Wein wieder näher bringen. Wir haben Ihnen unten auch ein paar Beispiele hochgeladen in welche Richtung es gehen könnte.
Wichtrig ist das auf unserem Flyer die Kontakdaten, Adresse sowie Instagramname zu finden sind. Nicht sehr groß unjd presänt am besten in einer Ecke.
Unser Logo sollte zu sehen sein. Muss aber nicht unbedingt in den Vordergrund. Die Zeiten sowie Essen und Getränke. Oder anstatt die Getränke gleich eine passende Überschrift wie Gutsauschank oder ähnliches. Auch ein entworfenes Logo wie unten in den Beispielen könnten wir uns vorstellen.
Der flyer allgemein sollte nicht all zu viel Text haben.

```html
<!DOCTYPE html>
<html lang="de">
<head>
<meta charset="utf-8">
<title>Gutsausschank 2025 – Weingut Kolbe</title>
<link rel="stylesheet" href="https://fonts.googleapis.com/css2?family=Abril+Fatface&family=Alegreya+Sans:ital,wght@0,400;0,700;0,800;1,400&display=swap">
<style>
  :root {
    --page-bg: #ece8e3;
    --paper: #ffffff;
    --stripe: #f7efe6;
    --ink: #111111;
    --logo-ink: #2a2a2f;
    --grape: #70324f;
    --grape-light: #8a4a68;
  }
  * { margin: 0; padding: 0; box-sizing: border-box; }
  html, body {
    width: 750px; height: 1200px; overflow: hidden;
    background: var(--page-bg);
  }
  .flyer {
    position: absolute; left: 75px; top: 0;
    width: 600px; height: 1200px;
    background: var(--paper);
    overflow: hidden;
    font-family: "Alegreya Sans", "Fira Sans", sans-serif;
    color: var(--ink);
  }
  .flyer__art { position: absolute; inset: 0; }
  .stripe { fill: var(--stripe); }
  .frame-line { stroke: var(--ink); stroke-width: 2.6; fill: none; }
  .headline-arc {
    font-family: "Abril Fatface", "Playfair Display", serif;
    font-size: 56px; fill: var(--ink);
  }

  .text { position: absolute; line-height: 1; white-space: nowrap; }
  .estate-label { top: 340px; font-size: 21px; letter-spacing: 0.3px; }
  .estate-label--left { left: 70px; }
  .estate-label--right { right: 70px; }

  .year {
    top: 448px; left: 0; width: 600px; text-align: center;
    font-family: "Abril Fatface", "Playfair Display", serif;
    font-size: 60px; font-weight: 400;
  }
  .tagline {
    top: 522px; left: 0; width: 600px; text-align: center;
    font-style: italic; font-size: 27px; line-height: 32px; letter-spacing: 0.4px;
  }

  .season { top: 797px; font-size: 26px; line-height: 31px; letter-spacing: 0.3px; }
  .season--dates { right: 323px; text-align: right; }
  .season--hours { left: 324px; }
  .season-divider { position: absolute; left: 299px; top: 785px; width: 2.6px; height: 108px; background: var(--ink); }

  .brand-name {
    top: 970px; left: 0; width: 600px; text-align: center;
    font-weight: 800; font-size: 42px; letter-spacing: 4px; color: var(--logo-ink);
  }
  .address {
    top: 1052px; left: 0; width: 600px; text-align: center;
    font-size: 19px; line-height: 25px;
  }
  .website {
    top: 1135px; left: 0; width: 600px; text-align: center;
    font-weight: 700; font-size: 20px;
  }
</style>
</head>
<body>
<main class="flyer">
  <svg class="flyer__art" width="600" height="1200" viewBox="0 0 600 1200">
    <defs>
      <path id="headline-curve" d="M 82 360 A 218 218 0 0 1 518 360"/>
      <linearGradient id="grape-tone" x1="0" y1="0" x2="0" y2="1">
        <stop offset="0" stop-color="var(--grape-light)"/>
        <stop offset="1" stop-color="var(--grape)"/>
      </linearGradient>
    </defs>

    <g class="stripes">
      <polygon class="stripe" points="86,0 433,0 -767,1200 -1114,1200"/>
      <polygon class="stripe" points="724,0 1071,0 -129,1200 -476,1200"/>
      <polygon class="stripe" points="1362,0 1709,0 509,1200 162,1200"/>
    </g>

    <text class="headline-arc">
      <textPath href="#headline-curve" startOffset="50%" text-anchor="middle">GUTSAUSSCHANK</textPath>
    </text>

    <rect class="grape-illustration" x="226" y="200" width="174" height="190" rx="24"
          fill="url(#grape-tone)" role="img"
          aria-label="Illustration: Weintraube mit Weinblatt und Ranke in Bordeauxrot"/>

    <g class="frame">
      <polyline class="frame-line" points="73,417 73,1146 194,1146"/>
      <polyline class="frame-line" points="405,1146 527,1146 527,417"/>
    </g>
  </svg>

  <p class="text estate-label estate-label--left">WEINGUT</p>
  <p class="text estate-label estate-label--right">KOLBE</p>

  <h1 class="text year">2025</h1>
  <p class="text tagline">Pfälzer Weine aus eigenem Anbau &amp;<br>regionale Köstlichkeiten</p>

  <p class="text season season--dates">22. August<br>bis<br>2. November</p>
  <span class="season-divider"></span>
  <p class="text season season--hours">Jeden Mittwoch<br>bis Sonntag<br>14 – 20 Uhr</p>

  <p class="text brand-name">KOLBE</p>
  <p class="text address">Holunderstr. 62<br>76829 Rebental / Weinstraße</p>
  <p class="text website">www.wein-kolbe.de</p>
</main>
</body>
</html>
```